Brindlewood Lawn Care

I am looking for a postcard design for a lawn maintenance company. The postcards will be sent EDDM and have a size of 7"x 5" color, both sides. This company is relatively new. It is located in New Jersey, 08007. We maintain peoples properties at a reasonable cost. We pride ourselves in a no contract/ commitment during the season. Some of the work that is done includes: mowing, trimming, edging, application of fertilizers, weed control on the property, aeration of the soil, cutting of small trees, mulching, and hedging. We are fully licensed and insured. I do not approve of "Hurry in while this offer lasts" propaganda. I would like this postcard to be inviting. The phone number (604) 215- 9173, email BrindlewoodLawnCare@mailbox-example.com, and website (BrindlewoodLawnCare-example.com) should somehow be incorporated into the design.

Target Market(s)

Targeting people who are looking for lawn maintenance.

Industry/Entity Type

It Company

Requirements
Must have
• Subtle, welcoming design. The design must have phone number, email, and web address. Contracts are not mandatory, so that could be incorporated as well.
Nice to have
• Light, refreshing spring is in the air kind of feel.
Should not have
• Generic design similar to the "mundane"

```html
<!DOCTYPE html>
<html lang="en">
<head>
<meta charset="utf-8">
<title>Brindlewood Lawn Care – Postcard</title>
<link rel="stylesheet" href="https://fonts.googleapis.com/css2?family=Noto+Serif:wght@400;700&family=Playfair+Display:ital,wght@1,700&family=Roboto:ital,wght@0,700;1,900&display=swap">
<style>
  :root {
    --grass-deep: #0f1a07;
    --grass-mid: #3b4d14;
    --grass-light: #8a8f2a;
    --sun-core: #fffbe6;
    --sun-glow: #f3e7a0;
    --white: #ffffff;
    --accent-green: #39d12b;
    --badge-orange: #f4902a;
    --badge-ring: #fbd7a8;
    --panel-fill: rgba(255,255,255,0.12);
    --panel-line: rgba(255,255,255,0.85);
    --ink-dark: #111;
  }
  * { margin: 0; padding: 0; box-sizing: border-box; }
  html, body { width: 1200px; height: 929px; overflow: hidden; background: #fff; }
  .postcard {
    position: relative;
    width: 1200px; height: 929px;
    overflow: hidden;
    color: var(--white);
  }
  .hero-photo {
    position: absolute; inset: 0;
    background:
      radial-gradient(circle at 575px 300px, var(--sun-core) 0, var(--sun-glow) 60px, rgba(220,200,110,0.7) 170px, rgba(120,120,40,0.25) 380px, transparent 560px),
      linear-gradient(180deg, #2b3312 0%, var(--grass-mid) 35%, #2b3a0e 60%, var(--grass-deep) 100%);
  }
  .brand {
    position: absolute; left: 62px; top: 34px;
    font-family: "Noto Serif", serif;
    line-height: 1;
  }
  .brand-name { font-size: 40px; font-weight: 400; letter-spacing: 0.5px; }
  .brand-tag { font-size: 27px; margin-top: 6px; }

  .badge { position: absolute; left: 912px; top: 20px; width: 232px; height: 232px; }
  .badge-text {
    position: absolute; left: 912px; top: 20px; width: 232px; height: 232px;
    display: flex; flex-direction: column; align-items: center; justify-content: center;
    font-family: "Roboto", sans-serif; font-weight: 900; font-style: italic;
    color: var(--white); transform: rotate(-18deg); line-height: 0.95; text-align: center;
  }
  .badge-text .big { font-size: 36px; }
  .badge-text .small { font-size: 24px; }

  .services {
    position: absolute; left: 10px; top: 165px; width: 290px; height: 535px;
    border: 2px solid var(--panel-line); border-radius: 26px;
    background: var(--panel-fill);
    padding: 14px 0 0 20px;
  }
  .services-title { display: flex; align-items: flex-end; gap: 8px; margin-bottom: 8px; }
  .services-title .script {
    font-family: "Playfair Display", serif; font-style: italic; font-weight: 700; font-size: 62px; line-height: 0.9;
  }
  .services-title .rest {
    font-family: "Noto Serif", serif; font-size: 18px; line-height: 1.05; padding-bottom: 4px;
  }
  .service-list { list-style: none; }
  .service-list li {
    display: flex; align-items: center; gap: 14px;
    height: 58px;
    font-family: "Noto Serif", serif; font-size: 17px; line-height: 1.05;
  }
  .service-list svg { flex: none; width: 40px; height: 40px; }

  .headline {
    position: absolute; left: 318px; top: 438px; width: 840px;
    text-align: center;
    font-family: "Roboto", sans-serif; font-weight: 900; font-style: italic;
    font-size: 58px; line-height: 1.04;
    text-shadow: 3px 3px 0 var(--ink-dark);
  }
  .headline .greener { color: var(--accent-green); }

  .contact {
    position: absolute; left: 318px; top: 720px; width: 800px;
    text-align: center; font-family: "Roboto", sans-serif;
  }
  .contact-call { font-size: 36px; font-weight: 700; letter-spacing: 1px; }
  .contact-phone { font-size: 68px; font-weight: 700; letter-spacing: 2px; line-height: 1.05; margin-top: -4px; }
  .contact-line { font-family: "Noto Serif", serif; font-size: 30px; line-height: 1.35; }
</style>
</head>
<body>
<main class="postcard">
  <div class="hero-photo" role="img" aria-label="Close-up photograph of tall lawn grass backlit by bright sunlight"></div>

  <header class="brand">
    <div class="brand-name">BrindlewoodLawnCare</div>
    <div class="brand-tag">lawn maintenance company</div>
  </header>

  <svg class="badge" viewBox="0 0 232 232" aria-hidden="true">
    <polygon fill="var(--badge-orange)" points="116,4 131,20 150,9 160,28 181,23 185,44 206,45 204,66 224,73 216,93 232,107 219,123 230,141 212,151 216,172 195,176 193,197 172,195 163,215 144,206 130,224 116,208 102,224 88,206 69,215 60,195 39,197 37,176 16,172 20,151 2,141 13,123 0,107 16,93 8,73 28,66 26,45 47,44 51,23 72,28 82,9 101,20"/>
    <circle cx="116" cy="116" r="84" fill="none" stroke="var(--badge-ring)" stroke-width="4"/>
  </svg>
  <div class="badge-text">
    <span class="big">Fully</span>
    <span class="big">Licensed</span>
    <span class="small">and</span>
    <span class="big">insured</span>
  </div>

  <section class="services">
    <div class="services-title">
      <span class="script">Our</span>
      <span class="rest">Works<br>included:</span>
    </div>
    <ul class="service-list">
      <li><svg viewBox="0 0 40 40"><circle cx="20" cy="20" r="19" fill="var(--white)"/><rect x="10" y="18" width="18" height="8" rx="2" fill="var(--ink-dark)"/><circle cx="13" cy="28" r="3" fill="var(--ink-dark)"/><circle cx="26" cy="28" r="3" fill="var(--ink-dark)"/><path d="M28 18 L32 10" stroke="var(--ink-dark)" stroke-width="2"/></svg>Mowing</li>
      <li><svg viewBox="0 0 40 40"><circle cx="20" cy="20" r="19" fill="var(--white)"/><path d="M10 28 L26 14 M14 12 L30 26" stroke="var(--ink-dark)" stroke-width="3"/></svg>Trimming</li>
      <li><svg viewBox="0 0 40 40"><circle cx="20" cy="20" r="19" fill="var(--white)"/><path d="M9 16 H31 M9 22 H31 M9 28 H31" stroke="var(--ink-dark)" stroke-width="2.5"/></svg>Edging</li>
      <li><svg viewBox="0 0 40 40"><circle cx="20" cy="20" r="19" fill="var(--white)"/><rect x="14" y="10" width="12" height="20" rx="3" fill="var(--ink-dark)"/></svg>Application<br>of fertilizers</li>
      <li><svg viewBox="0 0 40 40"><circle cx="20" cy="20" r="19" fill="var(--white)"/><path d="M20 30 V16 M20 20 Q12 18 12 10 Q20 12 20 20 M20 22 Q28 20 28 12 Q20 14 20 22" stroke="var(--ink-dark)" stroke-width="2" fill="none"/></svg>Weed control</li>
      <li><svg viewBox="0 0 40 40"><circle cx="20" cy="20" r="19" fill="var(--white)"/><circle cx="14" cy="16" r="2.5" fill="var(--ink-dark)"/><circle cx="26" cy="16" r="2.5" fill="var(--ink-dark)"/><circle cx="14" cy="26" r="2.5" fill="var(--ink-dark)"/><circle cx="26" cy="26" r="2.5" fill="var(--ink-dark)"/><circle cx="20" cy="21" r="2.5" fill="var(--ink-dark)"/></svg>Aeration of<br>the soil</li>
      <li><svg viewBox="0 0 40 40"><circle cx="20" cy="20" r="19" fill="var(--white)"/><path d="M20 8 L29 24 H11 Z" fill="var(--ink-dark)"/><rect x="18" y="24" width="4" height="8" fill="var(--ink-dark)"/></svg>Cutting of<br>small trees</li>
      <li><svg viewBox="0 0 40 40"><circle cx="20" cy="20" r="18" fill="none" stroke="var(--white)" stroke-width="2.5"/><path d="M20 11 V29 M11 20 H29" stroke="var(--white)" stroke-width="3"/></svg>And more...</li>
    </ul>
  </section>

  <h1 class="headline">The grass will<br>never be <span class="greener">GREENER</span><br>on the other<br>side anymore!</h1>

  <section class="contact">
    <div class="contact-call">CALL</div>
    <div class="contact-phone">(604) 215- 9173</div>
    <div class="contact-line">BrindlewoodLawnCare@mailbox-example.com</div>
    <div class="contact-line">BrindlewoodLawnCare-example.com</div>
  </section>
</main>
</body>
</html>
```